Business Card Design Project

We are a innovative residential building company based in Sydney, Australia
our business name is MORWEN CRAFTWORKS SOLUTIONS PTY LTD.
Our company by line (please incorporate) "Shaping Homes, Made to Last!"
We specialise in creating high end innovative residential Alterations & Additions for our clients.
We would like to see original high end designs that are professional, striking, creative & have the WOW factor...
We like BLACK, BLUE, ORANGE, WHITE, SILVER... We would like to convey to our clients - professionalism/innovative approach/design/creativity/assurance/wow factor...

Target Market(s)

Clients who want/need residential alterations or additions to their homes.

Industry/Entity Type

Residential

Requirements
Must have
• LOGO
Bi Line (somewhere)
Name
Title
Phone number
Email address

Member of the NHG (Northern Homecraft Guild) Logo
Web Address - www.morwencraftworks.com.au

Nice to have
• Fantail's are a small New Zealand bird and we would like to incorporate this as part of our new companies (double sided) business card. Whether it be the bird or just it's (fan) tail!
Should not have
• anything old-style.
we are looking for a contemporary, modern & striking Business Cards
clear strong colour accents
we had some stunning designs sent through, our favourites used the birds tail as an imprint on the card (not sure if that is clear of not)

```html
<!DOCTYPE html>
<html lang="en">
<head>
<meta charset="utf-8">
<title>Morwen Craftworks Solutions – Business Card</title>
<link href="https://fonts.googleapis.com/css2?family=Barlow+Semi+Condensed:wght@600&family=Open+Sans:wght@400;700&display=swap" rel="stylesheet">
<style>
  :root {
    --backdrop: #e4e2de;
    --band-blue: #0a88c2;
    --card-orange: #f9a825;
    --card-orange-deep: #f29a12;
    --imprint: #e8921a;
    --ink-dark: #2a2a2a;
    --ink-grey: #6b5a3a;
    --paper-white: #ffffff;
    --edge-shadow: rgba(0, 0, 0, 0.28);
  }
  * { box-sizing: border-box; margin: 0; padding: 0; }
  html, body {
    width: 1200px;
    height: 533px;
    overflow: hidden;
    background: var(--backdrop);
  }
  .canvas {
    position: relative;
    width: 1200px;
    height: 533px;
  }
  .card {
    position: absolute;
    top: 116px;
    width: 520px;
    height: 300px;
    background: var(--card-orange);
    box-shadow: 0 6px 14px var(--edge-shadow);
    overflow: hidden;
  }
  .card--front { left: 50px; }
  .card--back {
    left: 630px;
    background: linear-gradient(120deg, var(--card-orange) 55%, var(--card-orange-deep) 100%);
  }

  /* Front */
  .brand-band {
    position: absolute;
    inset: 0 0 auto 0;
    height: 92px;
    background: var(--band-blue);
    box-shadow: 0 4px 8px rgba(0, 0, 0, 0.25);
    padding: 22px 24px 0 24px;
  }
  .brand-name {
    display: flex;
    align-items: center;
    gap: 10px;
    font-family: "Barlow Semi Condensed", "Arial Narrow", sans-serif;
    font-weight: 600;
    font-size: 24px;
    letter-spacing: 0.2px;
    color: var(--paper-white);
    white-space: nowrap;
  }
  .brand-mark {
    width: 14px;
    height: 14px;
    background: var(--paper-white);
    flex: none;
  }
  .brand-tagline {
    margin: 4px 0 0 24px;
    font-family: "Open Sans", Arial, sans-serif;
    font-size: 12px;
    color: var(--paper-white);
  }
  .tail-imprint {
    position: absolute;
    left: 296px;
    top: 108px;
    width: 150px;
    height: 86px;
    background: var(--imprint);
    border-radius: 40px 46px 20px 20px;
    opacity: 0.7;
  }
  .contact {
    position: absolute;
    left: 44px;
    top: 196px;
    display: grid;
    grid-template-columns: 70px auto;
    row-gap: 1px;
    font-family: "Open Sans", Arial, sans-serif;
    font-size: 11.5px;
    line-height: 15px;
    color: var(--ink-dark);
  }
  .contact dt { font-weight: 700; }
  .contact dd { font-weight: 400; }

  /* Back */
  .back-imprint {
    position: absolute;
    left: 70px;
    top: 60px;
    width: 320px;
    height: 200px;
    background: var(--imprint);
    border-radius: 48% 52% 40% 44%;
    opacity: 0.35;
  }
  .back-lockup {
    position: absolute;
    left: 0;
    right: 0;
    top: 118px;
    text-align: center;
  }
  .back-name {
    font-family: "Barlow Semi Condensed", "Arial Narrow", sans-serif;
    font-weight: 600;
    font-size: 23px;
    color: var(--ink-grey);
    white-space: nowrap;
  }
  .back-tagline {
    margin-top: 2px;
    font-family: "Open Sans", Arial, sans-serif;
    font-size: 12px;
    color: var(--ink-grey);
  }
</style>
</head>
<body>
<main class="canvas">
  <section class="card card--front" aria-label="Business card front">
    <header class="brand-band">
      <div class="brand-name"><span class="brand-mark"></span>MORWEN CRAFTWORKS SOLUTIONS PTY LTD</div>
      <p class="brand-tagline">Shaping Homes, Made to Last!</p>
    </header>
    <div class="tail-imprint" role="img" aria-label="Embossed bird tail imprint"></div>
    <dl class="contact">
      <dt>Name:</dt><dd>Daniel Harrow</dd>
      <dt>Title:</dt><dd>Architect</dd>
      <dt>E-mail:</dt><dd>daniel.harrow@morwencraftworks.com.au</dd>
      <dt>Telephone:</dt><dd>+61 (02) 5550 1847</dd>
    </dl>
  </section>

  <section class="card card--back" aria-label="Business card back">
    <div class="back-imprint" role="img" aria-label="Faint large bird silhouette decoration"></div>
    <div class="back-lockup">
      <p class="back-name">MORWEN CRAFTWORKS SOLUTIONS PTY LTD.</p>
      <p class="back-tagline">Shaping Homes, Made to Last!</p>
    </div>
  </section>
</main>
</body>
</html>
```